Summer Drinks Flyer for Coffee Shop

We are a coffee shop in London and would like to have a cool and nice flyer for our summer drinks (juices and frozen drink) flyer - see on the attached file for the list

Attached you can find an "attempt" - please note that I would no necessary need the image below.

I also attache our new logo.

thank you

```html
<!DOCTYPE html>
<html lang="en">
<head>
<meta charset="utf-8">
<title>Summer Drinks Menu</title>
<link rel="stylesheet" href="https://fonts.googleapis.com/css2?family=Oswald:wght@300&family=Italianno&display=swap">
<style>
  :root {
    --board: #0b0a08;
    --gold: #d2aa3c;
    --gold-edge: #b8902a;
    --frame: #fbfbf8;
  }
  html, body {
    margin: 0;
    padding: 0;
    width: 864px;
    height: 1200px;
    overflow: hidden;
    background: #efe9dd;
  }
  .menu {
    position: relative;
    width: 864px;
    height: 1200px;
    background: var(--board);
    overflow: hidden;
    font-family: "Oswald", "Arial Narrow", sans-serif;
    font-weight: 300;
    color: var(--gold);
  }
  .menu__edge {
    position: absolute;
    top: 0;
    right: 0;
    width: 15px;
    height: 100%;
    background: var(--gold-edge);
  }
  .photo {
    position: absolute;
    box-sizing: border-box;
    border: 9px solid var(--frame);
    box-shadow: 0 3px 8px rgba(0,0,0,.45);
  }
  .photo--smoothie {
    left: 22px; top: -6px; width: 296px; height: 352px;
    transform: rotate(-1deg);
    background: linear-gradient(160deg, #e9ecef 0%, #dfe3e6 30%, #d63a4a 45%, #c42437 70%, #e9ecef 100%);
  }
  .photo--juice {
    left: 14px; top: 306px; width: 356px; height: 520px;
    transform: rotate(1.5deg);
    background: linear-gradient(180deg, #2f8fd0 0%, #8fd0ef 25%, #f3b63a 45%, #f0a425 70%, #8c7a63 88%, #6f604d 100%);
  }
  .photo--coffee {
    left: 26px; top: 832px; width: 320px; height: 358px;
    transform: rotate(-1deg);
    background: linear-gradient(180deg, #0a0807 0%, #1a1410 20%, #e9d8c4 30%, #b98b63 55%, #6b4a2f 80%, #2a1b10 100%);
  }
  .brand {
    position: absolute;
    left: 430px;
    top: 118px;
    width: 340px;
    display: flex;
    align-items: center;
    justify-content: center;
    gap: 14px;
    font-size: 58px;
    letter-spacing: 1px;
    line-height: 1;
  }
  .brand__dot {
    width: 22px;
    height: 22px;
    border-radius: 50%;
    background: var(--gold);
  }
  .title {
    position: absolute;
    font-family: "Italianno", cursive;
    font-size: 58px;
    line-height: 1;
    margin: 0;
    font-weight: 400;
  }
  .title--first { left: 408px; top: 205px; }
  .title--second { left: 572px; top: 275px; }
  .section {
    position: absolute;
    left: 394px;
    width: 428px;
  }
  .section__head {
    display: flex;
    justify-content: space-between;
    align-items: baseline;
    font-size: 34px;
    line-height: 40px;
    margin: 0;
    font-weight: 300;
    padding: 0 5px 1px 0;
    border-bottom: 2px solid var(--gold);
  }
  .section__list {
    list-style: none;
    margin: 0;
    padding: 0;
    font-size: 28px;
  }
  .section__note {
    position: absolute;
    right: 8px;
    width: 150px;
    text-align: center;
    font-family: "Italianno", cursive;
    font-size: 25px;
    line-height: 24px;
  }
  .section--frozen { top: 400px; }
  .section--frozen .section__list { line-height: 44px; margin-top: 6px; }
  .section--juices { top: 599px; }
  .section--juices .section__list { line-height: 44px; margin-top: 10px; }
  .section--juices .section__note { top: 50px; }
  .section--coffee { top: 915px; }
  .section--coffee .section__list { line-height: 45px; margin-top: 12px; }
  .section--coffee .section__note { top: 52px; }
</style>
</head>
<body>
<main class="menu">
  <div class="menu__edge"></div>

  <div class="photo photo--smoothie" role="img" aria-label="Photo of a red frozen strawberry drink with a sprig of mint"></div>
  <div class="photo photo--juice" role="img" aria-label="Photo of a tall glass of orange juice with an orange slice, straw and cocktail umbrella on a beach"></div>
  <div class="photo photo--coffee" role="img" aria-label="Photo of an iced latte with whipped cream on coffee beans"></div>

  <div class="brand"><span class="brand__dot"></span><span class="brand__name">brioletta</span></div>

  <h1 class="title title--first">New Summer</h1>
  <h1 class="title title--second">Drinks Menu</h1>

  <section class="section section--frozen">
    <h2 class="section__head"><span>FROZEN FRUITS DRINK</span><span>£2.95</span></h2>
    <ul class="section__list">
      <li>Strawberry and banana</li>
      <li>Pineapple, mango and banana</li>
    </ul>
  </section>

  <section class="section section--juices">
    <h2 class="section__head"><span>FRUIT JUICES</span><span>£2.95</span></h2>
    <p class="section__note">Add Mint or Ginger<br>for Free!</p>
    <ul class="section__list">
      <li>Orange and carrot</li>
      <li>Orange and pineapple</li>
      <li>Pineapple and apple</li>
      <li>Apple and kiwi</li>
      <li>Carrot and ginger</li>
    </ul>
  </section>

  <section class="section section--coffee">
    <h2 class="section__head"><span>ICED COFFES</span><span>£2.45</span></h2>
    <p class="section__note">Add Syrup Shot<br>for 10p</p>
    <ul class="section__list">
      <li>Iced Coffee</li>
      <li>Iced Latte</li>
      <li>Iced Chocolate Drink</li>
    </ul>
  </section>
</main>
</body>
</html>
```